Texas Recycling and dump company needs Flyer design

We need a flyer design for a new company based in Austin Texas called 'Salvage Grove'. We receive dump materials on our property along with sell repurposed materials. We would like our design to include our logo along with add some creative designs to the flyer. Please use the attached image file as an outline. Blank boxes can be used for additional images.

Target Market(s)

Handing out flyers to new companies and hopefully getting contracts with them.

Font styles to use
Serif
Sans Serif

Requirements
Must have
• double sided
• images
Nice to have
• QR code with our website

```html
<!DOCTYPE html>
<html lang="en">
<head>
<meta charset="utf-8">
<title>Salvage Grove – Landscaping Materials Flyer</title>
<link rel="stylesheet" href="https://fonts.googleapis.com/css2?family=Arimo:ital,wght@0,400;0,700;1,700&display=swap">
<style>
  :root {
    --blue: #1f6fb8;
    --blue-dark: #1a5d9c;
    --green: #7cc242;
    --ink: #222222;
    --paper: #ffffff;
    --shadow: rgba(0,0,0,0.18);
  }
  * { box-sizing: border-box; margin: 0; padding: 0; }
  html, body { width: 855px; height: 1200px; overflow: hidden; background: var(--paper); }
  body { font-family: "Arimo", Arial, sans-serif; color: var(--ink); }
  .flyer { position: relative; width: 855px; height: 1200px; background: var(--paper); }

  .headline { position: absolute; top: 50px; left: 0; width: 100%; text-align: center; font-style: italic; font-weight: 700; line-height: 1.12; }
  .headline__main { color: var(--blue); font-size: 63px; letter-spacing: 0.3px; }
  .headline__sub { color: var(--green); font-size: 61px; }

  .materials { position: absolute; top: 255px; left: 123px; width: 610px;
    display: grid; grid-template-columns: repeat(4, 136px); column-gap: 22px; row-gap: 42px; }
  .material { text-align: center; }
  .material__frame { width: 136px; height: 136px; background: var(--blue); padding: 14px; box-shadow: 2px 3px 5px var(--shadow); }
  .material__photo { width: 100%; height: 100%; }
  .material__label { margin-top: 8px; font-size: 23px; line-height: 28px; color: var(--ink); }

  .photo--mulch { background: linear-gradient(135deg, #8a4a2a, #c27a4a 55%, #6b3720); }
  .photo--topsoil { background: linear-gradient(160deg, #5b4a36, #2e2418 60%, #6d5a40); }
  .photo--rocks { background: linear-gradient(180deg, #6e8a3c, #9aa07a 55%, #7b7466); }
  .photo--base { background: linear-gradient(135deg, #1e1e1e, #3a3a3a 50%, #151515); }
  .photo--grass { background: linear-gradient(180deg, #cfd8c8, #6b8f3e 50%, #4d6b2b); }
  .photo--asphalt { background: linear-gradient(135deg, #3b3f44, #9ba4ac 50%, #2d3135); }
  .photo--pavers { background: linear-gradient(135deg, #a97856, #d1a57e 50%, #8f6246); }
  .photo--pebbles { background: linear-gradient(135deg, #b9a184, #8d6b52 45%, #d7c6ad); }

  .extra { margin-top: -22px; width: 136px; height: 151px; background: var(--blue); color: var(--paper);
    font-size: 22px; line-height: 1.15; padding: 14px 6px; text-align: center; box-shadow: 2px 3px 5px var(--shadow); }

  .brand { position: absolute; top: 1004px; left: 100px; display: flex; align-items: center; gap: 12px; }
  .brand__dot { width: 30px; height: 30px; border-radius: 50%; background: var(--green); }
  .brand__name { font-size: 36px; font-weight: 700; color: var(--blue); letter-spacing: 1px; }

  .contact { position: absolute; top: 962px; left: 420px; width: 420px; font-style: normal; text-align: center;
    font-size: 20px; line-height: 1.4; color: var(--blue); white-space: nowrap; }

  .footer-band { position: absolute; left: 0; bottom: 18px; width: 100%; height: 18px; background: var(--blue); }
  .footer-band::after { content: ""; position: absolute; left: 0; top: 24px; width: 100%; height: 4px; background: var(--blue-dark); }
</style>
</head>
<body>
<main class="flyer">
  <header class="headline">
    <h1 class="headline__main">Landscaping Materials</h1>
    <p class="headline__sub">Hot Deals Daily!</p>
  </header>

  <section class="materials">
    <div class="material"><div class="material__frame"><div class="material__photo photo--mulch" role="img" aria-label="Photo of red wood mulch"></div></div><p class="material__label">Mulch</p></div>
    <div class="material"><div class="material__frame"><div class="material__photo photo--topsoil" role="img" aria-label="Photo of a hand holding top soil"></div></div><p class="material__label">Top Soil</p></div>
    <div class="material"><div class="material__frame"><div class="material__photo photo--rocks" role="img" aria-label="Photo of landscaping rocks in a garden"></div></div><p class="material__label">Rocks</p></div>
    <div class="material"><div class="material__frame"><div class="material__photo photo--base" role="img" aria-label="Photo of dark base material"></div></div><p class="material__label">Base</p></div>

    <div class="material"><div class="material__frame"><div class="material__photo photo--grass" role="img" aria-label="Photo of decorative grass in a planter"></div></div><p class="material__label">Dec. Grass</p></div>
    <div class="material"><div class="material__frame"><div class="material__photo photo--asphalt" role="img" aria-label="Photo of an asphalt surface"></div></div><p class="material__label">Asphalt</p></div>
    <div class="material"><div class="material__frame"><div class="material__photo photo--pavers" role="img" aria-label="Photo of a paver walkway"></div></div><p class="material__label">Pavers</p></div>
    <div class="material"><div class="material__frame"><div class="material__photo photo--pebbles" role="img" aria-label="Photo of colored pebbles"></div></div><p class="material__label">Pebbles</p></div>

    <div class="extra">Additional Materials Here or Hot Deal</div>
    <div class="extra">Additional Materials Here or Hot Deal</div>
    <div class="extra">Additional Materials Here or Hot Deal</div>
    <div class="extra">Additional Materials Here or Hot Deal</div>
  </section>

  <div class="brand">
    <span class="brand__dot"></span>
    <span class="brand__name">SALVAGE GROVE</span>
  </div>

  <address class="contact">
    1280 Cedar Hollow Rd. Millbrook, Ohio 43950<br>
    (740) 555-0148
  </address>

  <div class="footer-band"></div>
</main>
</body>
</html>
```